In Store POP Material Design

From: Derek Hollis
Sent: Wednesday, October 10, 2012 7:35 AM
To: 'Neil Carver'
Subject: Marketing Brief for K7 branding
We are looking to create a new look and feel for our Steadfast Coverage (k7) branded materials.
We sell extended service plans through retailers and manufacturers throughout North America.
The store sales personnel offer an extended warranty with the purchase of an Appliance, TV, computer, Camera etc.
We also want these materials to allow for us to include client logos so that we can leverage their brands to add value. I have included our old K7 brochure, a new concept for our Brixwell store clients and another client named Oxbow as reference
Our objective is to create in store tools (brochures, posters, stickers) etc to help the sales people close more sales. We are positioning our protection plans as part of a "total solution" sale. For example, if you buy a TV, you would also need to buy a mount, HDMI cable, screen cleaner etc. In our materials we want to illustrate this and help the sales person not only sell our warranty but the other accessories and services as well.
We also want to create a standard look and feel that is very info-graphic in nature. Heavy use of icons and a web 2.0 type of feel.
Have a look at some of these Infographics and you'll get an idea what I mean.
http://chartplume.example/wp-content/uploads/2012/05/HDTV-Comparison-LCD-vs.-Plasma.jpg
http://visualmarrow.example/wp-content/uploads/2011/04/Handset_Infographic_800px.jpg
My favorite sites are
http://www.graphlantern.example/
http://www.quillpixel.example/
You can reference info on our programs through our corporate website:
http://www.thenq8venture.example/extended-warranty-solutions
Bottom line, we want to create a new look and feel for the K7 brand and then tie whatever we come up with into both online and in-store materials.
The winner of this design contest will have plenty of work through this project as well as our other companies which you will find at: www.thehollisfold.example
Derek Hollis
Hollis Fold of Companies | www.thehollisfold.example
Q8 Ventures | HFX Manufacturing | GateKeeper Assurance
T: 1.555.318.2094 | M: 1.555.467.8130
E: derek.hollis@thehollisfold.example

```html
<!DOCTYPE html>
<html lang="en">
<head>
<meta charset="utf-8">
<title>K7 Steadfast Coverage Plan – In Store Poster</title>
<link rel="stylesheet" href="https://fonts.googleapis.com/css2?family=Oswald:wght@300;400&family=Titillium+Web:wght@300;400;600&display=swap">
<style>
  :root {
    --stage: #1b1b1b;
    --poster: #8b8b8b;
    --panel: #464646;
    --ink: #111111;
    --ink-soft: #222222;
    --paper: #ffffff;
    --teal: #0e6e78;
    --sky: #00a9e0;
    --grey-bar: #5d5d5e;
    --lime: #b5d334;
    --orange: #f7941d;
    --text-light: #eeeeee;
    --rule: #6a6a6a;
  }
  * { box-sizing: border-box; margin: 0; padding: 0; }
  html, body { width: 1200px; height: 900px; overflow: hidden; background: var(--stage); }
  body { position: relative; font-family: "Titillium Web", Arial, sans-serif; }

  .poster {
    position: absolute; left: 257px; top: 15px; width: 656px; height: 857px;
    background: var(--poster);
  }
  .poster > * { position: absolute; }

  /* Coverage timeline */
  .timeline { left: 30px; top: 30px; }
  .year-label {
    font-family: "Oswald", sans-serif; font-weight: 300; font-size: 12px;
    fill: var(--ink);
  }
  .timeline-mark {
    left: 146px; top: 322px; width: 170px; height: 26px;
    transform-origin: 0 0; transform: rotate(-90deg);
    font-family: "Oswald", sans-serif; font-weight: 300; font-size: 17px; line-height: 26px;
    color: var(--sky); white-space: nowrap;
  }
  .timeline-mark .mark-code { color: var(--ink); font-weight: 400; margin-right: 6px; }
  .warranty-label {
    left: 152px; top: 512px; width: 72px;
    transform-origin: 0 0; transform: rotate(-90deg);
    font-family: "Oswald", sans-serif; font-weight: 400; font-size: 10px; line-height: 11px;
    color: var(--ink); text-align: center;
  }

  /* Brand header */
  .brand { left: 244px; top: 22px; display: flex; align-items: center; gap: 10px; }
  .brand-code {
    font-family: "Titillium Web", sans-serif; font-weight: 600; font-size: 44px; line-height: 1;
    color: var(--ink);
  }
  .brand-name {
    font-family: "Titillium Web", sans-serif; font-weight: 600; font-size: 15px; line-height: 15px;
    color: var(--ink);
  }
  .tagline {
    left: 458px; top: 27px; width: 158px;
    font-size: 11px; line-height: 12px; color: var(--sky); text-align: center;
  }

  /* Key features card */
  .features-card {
    left: 244px; top: 117px; width: 412px; height: 366px;
    background: var(--panel); border-radius: 6px 0 0 6px; overflow: hidden;
  }
  .features-head {
    height: 68px; background: linear-gradient(#ffffff, #dcdcdc); text-align: center; padding-top: 8px;
  }
  .features-title {
    font-family: "Oswald", sans-serif; font-weight: 400; font-size: 26px; line-height: 28px; color: var(--sky);
  }
  .features-sub { font-family: "Oswald", sans-serif; font-weight: 300; font-size: 13px; line-height: 14px; color: var(--ink-soft); }
  .ring { position: absolute; left: 22px; top: 98px; }
  .footnote { position: absolute; left: 16px; bottom: 8px; font-size: 5.5px; color: var(--orange); }

  .feature { position: absolute; left: 272px; width: 126px; font-size: 6.5px; line-height: 7.6px; }
  .feature-title {
    display: inline-block; font-family: "Oswald", sans-serif; font-size: 8px; line-height: 9px;
    padding-bottom: 1px; margin-bottom: 3px; border-bottom: 1px solid currentColor; width: 100%;
  }
  .feature-home { top: 74px; color: var(--paper); }
  .feature-component { top: 138px; color: var(--sky); }
  .feature-food { top: 218px; color: var(--orange); }
  .feature-lemon { top: 290px; color: var(--lime); }
  .feature-title .icon { vertical-align: middle; margin-right: 4px; }

  /* Service steps */
  .service {
    left: 0; top: 557px; width: 314px; height: 255px;
    background: var(--panel); border-radius: 0 4px 4px 0; padding: 38px 20px 0 20px;
  }
  .service-title { font-family: "Oswald", sans-serif; font-weight: 400; font-size: 25px; line-height: 30px; color: var(--sky); margin-left: 6px; }
  .step {
    display: flex; align-items: flex-start; gap: 12px; color: var(--text-light);
    font-size: 14.5px; line-height: 15px; border-bottom: 1px solid var(--rule);
  }
  .step-one { margin-top: 22px; padding-bottom: 18px; }
  .step-two { padding-top: 18px; padding-bottom: 20px; }
  .step-num { flex: 0 0 16px; font-family: "Titillium Web", sans-serif; font-weight: 300; font-size: 30px; line-height: 30px; }
  .step-text { flex: 0 0 200px; padding-top: 2px; }
  .step-icon { margin-top: 2px; flex: none; }

  /* Benefits checklist */
  .benefits { left: 372px; top: 598px; list-style: none; }
  .benefits li {
    display: flex; align-items: center; gap: 18px;
    font-size: 16px; line-height: 22.6px; color: var(--text-light);
  }
</style>
</head>
<body>
  <main class="poster">
    <svg class="timeline" width="140" height="510" viewBox="0 0 140 510" aria-label="Coverage timeline from 1 to 5 years">
      <rect x="51" y="7" width="25" height="380" fill="var(--teal)"/>
      <rect x="76" y="7" width="25" height="380" fill="var(--sky)"/>
      <rect x="51" y="387" width="25" height="96" fill="var(--grey-bar)"/>
      <rect x="76" y="387" width="25" height="96" fill="var(--paper)"/>
      <polygon points="101,190 108,197 101,204" fill="var(--sky)"/>
      <polygon points="101,428 108,435 101,442" fill="var(--paper)"/>
      <g stroke="var(--ink)" stroke-width="0.8">
        <line x1="7" y1="52" x2="51" y2="52"/>
        <line x1="7" y1="149" x2="51" y2="149"/>
        <line x1="7" y1="245" x2="51" y2="245"/>
        <line x1="7" y1="341" x2="51" y2="341"/>
        <line x1="7" y1="438" x2="51" y2="438"/>
      </g>
      <text class="year-label" x="11" y="48">5 Years</text>
      <text class="year-label" x="11" y="145">4 Years</text>
      <text class="year-label" x="11" y="241">3 Years</text>
      <text class="year-label" x="11" y="337">2 Years</text>
      <text class="year-label" x="11" y="434">1 Year</text>
    </svg>
    <div class="timeline-mark"><span class="mark-code">K7</span>Extended Coverage</div>
    <div class="warranty-label">Standard<br>Manufacturer's<br>Warranty</div>

    <div class="brand">
      <span class="brand-code">K7</span>
      <span class="brand-name">Steadfast<br>Coverage<br>Plan</span>
    </div>
    <p class="tagline">Extends your warranty coverage for up to 5 years from the date of purchase</p>

    <section class="features-card">
      <header class="features-head">
        <h2 class="features-title">total solution</h2>
        <p class="features-sub">Key Features</p>
      </header>
      <svg class="ring" width="230" height="230" viewBox="0 0 230 230" aria-label="Key features ring chart">
        <circle cx="115" cy="115" r="110" fill="none" stroke="#cfcfcf" stroke-width="1" stroke-dasharray="2 3"/>
        <circle cx="115" cy="115" r="96" fill="none" stroke="#9a9a9a" stroke-width="0.8"/>
        <circle cx="115" cy="115" r="88" fill="none" stroke="var(--lime)" stroke-width="0.6" stroke-dasharray="2 3"/>
        <g transform="rotate(-150 115 115)" fill="none" stroke-width="28">
          <circle cx="115" cy="115" r="62" stroke="var(--paper)" stroke-dasharray="129.8 389.6"/>
          <circle cx="115" cy="115" r="62" stroke="var(--sky)" stroke-dasharray="0 129.8 97.4 389.6"/>
          <circle cx="115" cy="115" r="62" stroke="var(--orange)" stroke-dasharray="0 227.2 64.9 389.6"/>
          <circle cx="115" cy="115" r="62" stroke="var(--lime)" stroke-dasharray="0 292.1 97.5 389.6"/>
        </g>
        <circle cx="115" cy="115" r="46" fill="#7a7a7a"/>
        <circle cx="115" cy="115" r="40" fill="#333333" role="img" aria-label="Footprints icon area"/>
      </svg>
      <p class="footnote">*Refer to terms and conditions for further details</p>

      <div class="feature feature-home">
        <svg class="icon" width="26" height="24" viewBox="0 0 26 24" aria-hidden="true"><path d="M13 2 L24 12 H21 V22 H5 V12 H2 Z" fill="var(--paper)"/><rect x="11" y="15" width="4" height="7" fill="var(--panel)"/></svg>
        <p>All repair service for major appliances will be provided in your home by one of our Authorized Service Technicians.</p>
      </div>
      <div class="feature feature-component">
        <span class="feature-title"><svg class="icon" width="18" height="18" viewBox="0 0 18 18" aria-hidden="true"><rect x="1" y="1" width="16" height="16" fill="none" stroke="currentColor" stroke-width="1.4"/><rect x="4" y="6" width="10" height="8" fill="none" stroke="currentColor"/></svg>Major Component Coverage</span>
        <p>Most manufacturers have reduced major component coverage from 5 years to just 1. With K7, you can cover these components for up to 5 years.</p>
      </div>
      <div class="feature feature-food">
        <span class="feature-title"><svg class="icon" width="14" height="18" viewBox="0 0 14 18" aria-hidden="true"><rect x="2" y="4" width="10" height="13" fill="none" stroke="currentColor" stroke-width="1.4"/><line x1="0" y1="3" x2="14" y2="3" stroke="currentColor" stroke-width="1.4"/></svg>Food Spoilage</span>
        <p>K7 allows for $250 worth of frozen food replacement during the term of the extended coverage if food spoilage occurs due to your freezer's mechanical failure.*</p>
      </div>
      <div class="feature feature-lemon">
        <span class="feature-title"><svg class="icon" width="16" height="16" viewBox="0 0 16 16" aria-hidden="true"><ellipse cx="8" cy="8" rx="7" ry="5.5" fill="none" stroke="currentColor" stroke-width="1.4" transform="rotate(-35 8 8)"/></svg>Lemon Aid</span>
        <p>Our customer service representatives will arrange for the free replacement of the product if the same component fails three times.</p>
      </div>
    </section>

    <section class="service">
      <h2 class="service-title">Service in 2 Easy Steps</h2>
      <div class="step step-one">
        <span class="step-num">1</span>
        <p class="step-text">Call us at 1 (866) 555-0142<br>to troubleshoot the problem.</p>
        <svg class="step-icon" width="36" height="36" viewBox="0 0 36 36" aria-hidden="true"><circle cx="18" cy="18" r="15" fill="none" stroke="#2a2a2a" stroke-width="3" stroke-dasharray="70 25"/><path d="M11 10 l5 0 l1 5 l-3 2 q3 5 7 7 l2-3 l5 1 l0 5 q-12 1 -17 -17z" fill="#2a2a2a"/></svg>
      </div>
      <div class="step step-two">
        <span class="step-num">2</span>
        <p class="step-text">If repair is required, we<br>will direct you to the nearest authorized servicer or dispatch a technician to your home.</p>
        <svg class="step-icon" width="46" height="26" viewBox="0 0 46 26" aria-hidden="true"><rect x="8" y="3" width="22" height="15" fill="#2a2a2a"/><path d="M30 7 h8 l5 6 v5 h-13z" fill="#2a2a2a"/><circle cx="15" cy="21" r="3.5" fill="#2a2a2a"/><circle cx="36" cy="21" r="3.5" fill="#2a2a2a"/><g stroke="#2a2a2a" stroke-width="1.5"><line x1="0" y1="7" x2="6" y2="7"/><line x1="2" y1="11" x2="6" y2="11"/><line x1="0" y1="15" x2="6" y2="15"/></g></svg>
      </div>
    </section>

    <ul class="benefits">
      <li><svg width="10" height="9" viewBox="0 0 10 9" aria-hidden="true"><path d="M1 5 L4 8 L9 1" fill="none" stroke="var(--sky)" stroke-width="1.6"/></svg>Fully Insured for Your Protection</li>
      <li><svg width="10" height="9" viewBox="0 0 10 9" aria-hidden="true"><path d="M1 5 L4 8 L9 1" fill="none" stroke="var(--sky)" stroke-width="1.6"/></svg>Parts + Labour Coverage</li>
      <li><svg width="10" height="9" viewBox="0 0 10 9" aria-hidden="true"><path d="M1 5 L4 8 L9 1" fill="none" stroke="var(--sky)" stroke-width="1.6"/></svg>Toll-Free Support</li>
      <li><svg width="10" height="9" viewBox="0 0 10 9" aria-hidden="true"><path d="M1 5 L4 8 L9 1" fill="none" stroke="var(--sky)" stroke-width="1.6"/></svg>Fully Transferable</li>
      <li><svg width="10" height="9" viewBox="0 0 10 9" aria-hidden="true"><path d="M1 5 L4 8 L9 1" fill="none" stroke="var(--sky)" stroke-width="1.6"/></svg>Power Surge Protection</li>
      <li><svg width="10" height="9" viewBox="0 0 10 9" aria-hidden="true"><path d="M1 5 L4 8 L9 1" fill="none" stroke="var(--sky)" stroke-width="1.6"/></svg>No Deductible</li>
      <li><svg width="10" height="9" viewBox="0 0 10 9" aria-hidden="true"><path d="M1 5 L4 8 L9 1" fill="none" stroke="var(--sky)" stroke-width="1.6"/></svg>No Hidden Fees</li>
    </ul>
  </main>
</body>
</html>
```